Engineering group involved with fire safety needs a business card

We need a business card design for a company based in Greece called "Varotis Group". We are engineers and specialized technicians, operating the following : a) Fire fighting equipment trade b) Installation , Inspection & Maintenance of fire extinguishers and fire protection systems c) Occupational Health & Safety (Risk assessment & management/ Staff training). We need a clear and simple card design. I uploaded a draft I made, in order to give you an idea of the company and how I currently imagine the design of the card. I also uploaded the logo in .png file format. We are always open to different, new suggestions and ideas you may want to submit.
Target Market(s)
industries, companies, managers, retail clients
Industry/Entity Type
Fire Safety
Contact Information for Business Card
Addresses & phone numbers (headquarters + branch), logo, name (you can find all the details on the uploaded files!)
Colors
Designer to choose colors to be used in the design.
Look and feel
Each slider illustrates characteristics of the customer's brand and the style your logo design should communicate.

```html
<!DOCTYPE html>
<html lang="en">
<head>
<meta charset="utf-8">
<title>Varotis Group – Business Card</title>
<link rel="stylesheet" href="https://fonts.googleapis.com/css2?family=Lato:wght@400;700&family=Oswald:wght@500&display=swap">
<style>
  :root {
    --backdrop: #2b2b2b;
    --brand-red: #b00a0a;
    --deep-red: #a90606;
    --slate: #5e6466;
    --ink: #4a4a4a;
    --paper: #ffffff;
    --rule: #c9c9c9;
  }
  * { margin: 0; padding: 0; box-sizing: border-box; }
  html, body {
    width: 1200px; height: 1200px; overflow: hidden;
    background: var(--backdrop);
    font-family: "Lato", Arial, sans-serif;
  }
  .card {
    position: absolute; top: 310px; height: 593px;
    overflow: hidden; text-align: center;
  }
  .card-front { left: 234px; width: 364px; background: var(--paper); color: var(--ink); }
  .card-back { left: 627px; width: 369px; background: var(--deep-red); color: var(--paper); }

  .brand-mark {
    position: absolute; top: 50px; left: 150px;
    width: 64px; height: 64px; background: var(--brand-red);
  }
  .brand-name {
    position: absolute; top: 148px; left: 0; right: 0;
    font-weight: 700; font-size: 52px; line-height: 1;
    letter-spacing: 2px; color: var(--brand-red);
  }
  .brand-name span { display: block; font-size: 30px; letter-spacing: 6px; margin-top: 2px; }

  .details { position: absolute; top: 262px; left: 0; right: 0; font-size: 17px; line-height: 22px; }
  .person-name { font-weight: 700; font-size: 21px; color: var(--brand-red); }
  .divider { width: 226px; height: 1px; background: var(--rule); margin: 7px auto 10px; }
  .divider.lower { margin: 11px auto 12px; }
  .label { color: var(--brand-red); }
  .office-title { color: var(--brand-red); }
  .office + .office { margin-top: 9px; }

  .footer-band {
    position: absolute; left: 0; right: 0; bottom: 0; height: 51px;
    display: flex; align-items: center; justify-content: center;
    font-weight: 700; font-size: 16px; color: var(--paper);
  }
  .card-front .footer-band { background: var(--brand-red); }
  .card-back .footer-band { background: var(--slate); }

  .back-name {
    position: absolute; top: 170px; left: 0; right: 0;
    font-weight: 700; font-size: 62px; line-height: 1; letter-spacing: 2px;
  }
  .back-name span { display: block; font-size: 36px; letter-spacing: 7px; margin-top: 2px; }
  .tagline {
    position: absolute; top: 278px; left: 0; right: 0; line-height: 24px;
    font-family: "Oswald", "Arial Narrow", sans-serif; font-weight: 500;
    font-size: 17px; letter-spacing: 0;
  }
  .services {
    position: absolute; top: 423px; left: 0; right: 0;
    list-style: none; font-size: 17.5px; line-height: 26.5px;
  }
</style>
</head>
<body>
  <section class="card card-front">
    <div class="brand-mark" aria-hidden="true"></div>
    <div class="brand-name">VAROTIS<span>GROUP</span></div>

    <div class="details">
      <p class="person-name">NIKOS DIMARAS</p>
      <p class="person-role">Mechanical Engineer- OHS Consultant</p>
      <div class="divider"></div>
      <p class="contact-line"><span class="label">M:</span> +30 690 000 12 34</p>
      <p class="contact-line"><span class="label">E:</span> nikos.dimaras@varotisgroup.gr</p>
      <div class="divider lower"></div>

      <div class="office">
        <p class="office-title">Headquarters:</p>
        <p>12 Akti Limenos, 19500 Lavrio</p>
        <p><span class="label">T:</span> +30 22920 10000</p>
      </div>
      <div class="office">
        <p class="office-title">Branch Office:</p>
        <p>48 Odos Kifisias, 15124 Marousi</p>
        <p><span class="label">T:</span> +30 210 0000100</p>
      </div>
    </div>

    <div class="footer-band">www.varotisgroup.gr</div>
  </section>

  <section class="card card-back">
    <div class="back-name">VAROTIS<span>GROUP</span></div>
    <p class="tagline">INSTALLATION - INSPECTION - MAINTENANCE</p>
    <ul class="services">
      <li>FIRE FIGHTING EQUIPMENT</li>
      <li>LICENSING &amp; BUSINESS REGISTRATION</li>
      <li>OCCUPATIONAL HEALTH &amp; SAFETY</li>
      <li>STAFF TRAINING</li>
    </ul>
    <div class="footer-band">info@varotisgroup.gr</div>
  </section>
</body>
</html>
```